Talvor GmbH business card

We Talvor GmbH based in Switzerland are looking for a business card design. The Fresh Jung, appealing to customers of all kinds. We already have a logo to upload but still a business card. Details: Talvor GmbH Address: Lindenweg 14b in 9476 Brugwil. Tel: 41 79 462 37 18, web: Talvor.ch, E-mail: info@Talvor.ch Facebook: Talvor GmbH. I am the Managing Director: Luka Petrovac. On reverse: Title: Transporter and bus rental Gross: Without deposit Super prices
Contact Information for Business Card
Siehe Projektbeschreibung
Requirements
Should not have
- Other pictures

```html
<!DOCTYPE html>
<html lang="de">
<head>
<meta charset="utf-8">
<title>Talvor GmbH – Visitenkarte</title>
<link rel="stylesheet" href="https://fonts.googleapis.com/css2?family=Poppins:wght@300;400;600;700&display=swap">
<style>
  :root {
    --page-bg: #e7e9ec;
    --card-white: #ffffff;
    --blue-light: #4a6799;
    --blue-mid: #3b5686;
    --blue-dark: #2c416c;
    --navy: #262a6b;
    --steel: #8fa3c4;
    --text-light: #e9eef7;
    --text-soft: #c3cfe3;
    --shadow: rgba(20, 30, 50, 0.25);
  }
  * { box-sizing: border-box; margin: 0; padding: 0; }
  html, body { width: 1200px; height: 900px; overflow: hidden; }
  body {
    background: var(--page-bg);
    font-family: "Poppins", sans-serif;
    display: flex;
    align-items: center;
    justify-content: center;
    gap: 40px;
  }
  .card {
    position: relative;
    width: 540px;
    height: 310px;
    background: var(--card-white);
    box-shadow: 0 10px 30px var(--shadow);
    overflow: hidden;
  }
  .card-art { position: absolute; inset: 0; width: 100%; height: 100%; z-index: 0; }
  .card > :not(.card-art) { z-index: 1; }

  /* Reverse side */
  .brand-mark {
    position: absolute;
    display: flex;
    align-items: center;
    gap: 10px;
    font-weight: 600;
    letter-spacing: 0.04em;
  }
  .back .brand-mark {
    top: 58px; right: 58px;
    color: var(--text-light);
    font-size: 34px;
  }
  .brand-mark .mark-square {
    width: 18px; height: 18px;
    background: currentColor;
  }
  .back .company {
    position: absolute;
    left: 40px; top: 196px;
  }
  .company-name {
    display: flex;
    align-items: flex-start;
    gap: 6px;
    font-weight: 700;
    font-size: 34px;
    color: var(--blue-mid);
    letter-spacing: 0.06em;
    line-height: 1;
  }
  .company-name small {
    font-size: 11px;
    font-weight: 600;
    letter-spacing: 0.08em;
    line-height: 1;
    margin-top: 2px;
  }
  .company-tagline {
    margin-top: 8px;
    font-size: 13px;
    font-weight: 400;
    color: var(--blue-mid);
    line-height: 1.35;
  }

  /* Front side */
  .front .brand-mark {
    top: 122px; left: 42px;
    color: var(--navy);
    font-size: 30px;
  }
  .person {
    position: absolute;
    left: 292px; top: 58px; right: 0;
  }
  .person-name {
    font-size: 17px;
    font-weight: 600;
    color: var(--text-light);
    display: flex;
    align-items: center;
    gap: 6px;
  }
  .person-name .surname { color: var(--navy); }
  .person-name::after {
    content: "";
    flex: 1;
    height: 1px;
    background: var(--steel);
    margin-left: 6px;
  }
  .person-role {
    font-size: 10px;
    font-weight: 300;
    color: var(--text-soft);
    letter-spacing: 0.03em;
  }
  .contact-list {
    position: absolute;
    left: 292px; top: 168px;
    list-style: none;
  }
  .contact-list li {
    display: flex;
    align-items: flex-start;
    gap: 14px;
    font-size: 9.5px;
    font-weight: 300;
    color: var(--text-light);
    line-height: 1.25;
    margin-bottom: 4px;
  }
  .contact-icon { width: 9px; height: 9px; flex: none; margin-top: 1px; fill: var(--text-soft); }
</style>
</head>
<body>

  <section class="card back" aria-label="Rückseite">
    <svg class="card-art" viewBox="0 0 540 310" aria-hidden="true">
      <defs>
        <linearGradient id="backPanel" x1="0" y1="0" x2="1" y2="1">
          <stop offset="0" stop-color="#4f6ea3"/>
          <stop offset="1" stop-color="#283a72"/>
        </linearGradient>
      </defs>
      <polygon points="360,250 540,180 540,230 400,262" fill="#3c5a90"/>
      <polygon points="190,0 540,0 540,180 360,250" fill="url(#backPanel)"/>
    </svg>
    <div class="brand-mark"><span class="mark-square"></span>Talvor</div>
    <div class="company">
      <div class="company-name"><span>TALVOR</span><small>GmbH</small></div>
      <div class="company-tagline">Transporter- &amp; Bus Vermietung<br>Ohne Kaution · Super Preise</div>
    </div>
  </section>

  <section class="card front" aria-label="Vorderseite">
    <svg class="card-art" viewBox="0 0 540 310" aria-hidden="true">
      <defs>
        <linearGradient id="frontPanel" x1="0" y1="0" x2="1" y2="1">
          <stop offset="0" stop-color="#4a6799"/>
          <stop offset="1" stop-color="#2f4572"/>
        </linearGradient>
      </defs>
      <rect width="540" height="310" fill="url(#frontPanel)"/>
      <polygon points="236,0 258,0 232,310 206,310" fill="#262a6b"/>
      <polygon points="0,0 236,0 212,310 0,310" fill="#ffffff"/>
    </svg>
    <div class="brand-mark"><span class="mark-square"></span>Talvor</div>

    <div class="person">
      <div class="person-name"><span>Luka</span><span class="surname">Petrovac</span></div>
      <div class="person-role">Geschäftsführer</div>
    </div>

    <ul class="contact-list">
      <li>
        <svg class="contact-icon" viewBox="0 0 10 10"><path d="M2 0.5 L3.6 2.6 L2.8 3.6 Q3.8 5.6 6.2 7 L7.3 6.3 L9.5 8 L8.3 9.5 Q4.5 9.2 1.8 5.8 Q0.3 3.6 0.6 1.6 Z"/></svg>
        +41 79 462 37 18
      </li>
      <li>
        <svg class="contact-icon" viewBox="0 0 10 10"><path d="M0.5 2 H9.5 V8 H0.5 Z M0.8 2.3 L5 5.4 L9.2 2.3" stroke="#e9eef7" stroke-width="0.6"/></svg>
        info@Talvor.ch
      </li>
      <li>
        <svg class="contact-icon" viewBox="0 0 10 10"><path d="M5 0.8 L9.5 5 H8 V9.2 H6 V6.5 H4 V9.2 H2 V5 H0.5 Z"/></svg>
        Talvor.ch
      </li>
      <li>
        <svg class="contact-icon" viewBox="0 0 10 10"><rect x="0.5" y="0.5" width="9" height="9" rx="1"/></svg>
        Talvor GmbH
      </li>
      <li>
        <svg class="contact-icon" viewBox="0 0 10 10"><path d="M5 9.6 Q1.5 5.6 1.5 3.6 A3.5 3.5 0 0 1 8.5 3.6 Q8.5 5.6 5 9.6 Z M5 2.3 A1.3 1.3 0 1 0 5 4.9 A1.3 1.3 0 1 0 5 2.3 Z" fill-rule="evenodd"/></svg>
        Lindenweg 14b in 9476<br>Brugwil
      </li>
    </ul>
  </section>

</body>
</html>
```